依頼詳細
【サイトの最大の要望】
①未経験の20代の求職者の登録者を増やす。
(短大卒・新卒・第二新卒・インターンシップの大学生)
②特に東京23区のエリアの強化

【強み】
・人材教育型採用支援
・未経験でも取れる
・アカデミー(代表自体が話す)

【ターゲット】
10代~20代の経理未経験者
(どちらかというと女性)
経理未経験の短大卒・新卒・第二新卒・インターンシップの大学生

【デザインについて】
・デザインテイストは「 モダン/ナチュラル/優しい/シンプル/清潔な/少し重厚感/ちょっと派手」

【参考サイト】
https://mofam.jp/
https://www.joblinvo.com/
https://senokuruto.jp/

【サイトマップ】
下記URL内のサイトマップを参照ください。
https://3.filebako.example/0722-b83d1e9a04fc2b67d51a0e4c88f7d2b1

■TOPページにGメニューとは別にデザインの入り口を必須で設けて頂きたいコン

テンツは以下となります。
(それ以外のページに関してはワークポッカーにお任せします)

サイトURL
http://tenuvel.com/
ページ数
1ページ
希望イメージ
シンプル 複雑
単色 カラフル
暗い 明るい
日常 高級
遊び心 厳粛
未来的 伝統的
女性的 男性的
希望する色
緑系、黄・オレンジ系、グレー系、黄・オレンジ系/グレー系/緑系(さし色)/ピンクベージュ
納品ファイル
• イラストレーター形式 (.ai)
• フォトショップ形式 (.psd)
• PNG形式 (.png)
補足説明
【店舗へのご連絡はおやめください】
ワークポッケ規約にもありますが、店舗への通常業務に支障が出るため、
直接電話等のお問い合わせをお控え頂きますよう、ご協力願います。

【素材写真】
下記よりダウンロードしてご使用ください。

また、ピクセモのカンプ画像をご使用ください。
選定後に正規データをお渡し致します。
(画像はマンスリーパック内でお願い致します。)
ワイヤーフレームを添付しますので、
参照ください。
先程の追記では説明不足でしてので、
補足致します。

サイトマップが確定する前に作成したワイヤーフレームになります。
決定版サイトマップを基に作成頂ければと思います。

ワイヤーフレームを添付することでデザインが全て同じになってしまう事を
避けたかったので、このタイミングで添付致しました。

ワイヤーフレームはあくまで参考として認識頂ければと思います。

宜しくお願い致します。

デザインの構成や色合いがとても素敵で訴求したいターゲットにも合っていると思いました。

選定させて頂きました。

引き続き、宜しくお願い致します。

```html
<!DOCTYPE html>
<html lang="ja">
<head>
<meta charset="utf-8">
<title>そよかぜキャリア｜未経験から経理のプロへ</title>
<link rel="stylesheet" href="https://fonts.googleapis.com/css2?family=Noto+Sans+JP:wght@400;500;700;900&family=Montserrat:wght@400;600;700&display=swap">
<style>
:root{
  --orange:#f39a2b;
  --orange-deep:#ee8a17;
  --green:#8cc63f;
  --ink:#333333;
  --sub:#777777;
  --line:#dddddd;
  --sky:#d8ebf4;
  --sky-ink:#2e6f98;
  --pale:#f4f4f4;
  --footer:#ffffff;
  --copy:#8c8c8c;
  --white:#ffffff;
}
*{box-sizing:border-box;margin:0;padding:0}
html,body{width:1200px;height:4800px;overflow:hidden}
body{font-family:"Noto Sans JP",sans-serif;color:var(--ink);background:var(--white);font-size:15px;line-height:1.7}
.en{font-family:"Montserrat",sans-serif}
.photo{display:block}

/* header */
.site-header{height:72px;display:flex;align-items:center;justify-content:space-between;padding:0 40px}
.brand{display:flex;align-items:center;gap:12px}
.brand-mark{width:30px;height:30px;border-radius:50%;background:var(--orange)}
.brand-text small{display:block;font-size:10px;color:var(--sub);line-height:1.2}
.brand-text strong{display:block;font-size:21px;font-weight:700;color:var(--orange);line-height:1.2}
.gnav{display:flex;gap:34px;font-size:14px;font-weight:500}

/* hero */
.hero{position:relative;height:708px;background:linear-gradient(180deg,#eef3f7 0%,#dfe7ee 55%,#c9d2da 100%)}
.hero .photo{position:absolute;inset:0}
.hero-copy{position:absolute;top:92px;left:0;right:0;text-align:center;font-size:54px;font-weight:900;line-height:1.45;letter-spacing:.06em;color:#222}
.hero-tabs{position:absolute;left:170px;right:170px;bottom:0;display:flex;gap:40px}
.hero-tab{flex:1;height:64px;display:flex;align-items:center;justify-content:center;font-size:20px;font-weight:700}
.hero-tab.is-seeker{background:var(--white);color:var(--orange);border-top:4px solid var(--orange)}
.hero-tab.is-company{background:var(--sky);color:var(--sky-ink)}

/* intro */
.intro{height:360px;display:flex;padding:34px 170px 0}
.intro-body{width:420px;padding-right:40px}
.intro-title{font-size:25px;font-weight:700;line-height:1.5;border-left:6px solid var(--orange);padding-left:16px;margin-bottom:20px}
.intro-text{font-size:12px;color:var(--sub);line-height:1.9}
.btn-more{display:inline-block;margin-top:22px;background:var(--orange);color:var(--white);font-size:13px;padding:6px 40px;border-radius:3px}
.intro .photo{width:440px;height:290px;background:linear-gradient(135deg,#f2efe9,#d8d2c8)}

/* photo strip */
.strip{height:300px;display:flex}
.strip .photo{flex:1}
.strip .p1{background:linear-gradient(135deg,#cfc9bf,#9c948a)}
.strip .p2{background:linear-gradient(135deg,#f1f1ef,#bfc3c6)}
.strip .p3{background:linear-gradient(135deg,#b5b0a8,#6f6a64)}

/* section titles */
.sec-title{text-align:center;font-size:30px;font-weight:700;line-height:1.3}
.sec-sub{display:block;text-align:center;font-size:12px;letter-spacing:.18em;margin-top:6px;color:var(--sub)}

/* reasons */
.reasons{height:320px;background:var(--orange);padding-top:30px;color:var(--white)}
.reasons .sec-title{color:var(--white)}
.reasons .sec-sub{color:var(--white)}
.reason-list{display:flex;justify-content:center;gap:52px;margin-top:28px}
.reason{width:150px;height:150px;border-radius:50%;background:var(--white);color:var(--orange);display:flex;flex-direction:column;align-items:center;justify-content:center}
.reason-label{font-size:12px;font-weight:700;line-height:1.35;text-align:center}
.reason-num{font-size:50px;font-weight:700;line-height:1.1}
.reason-num span{font-size:18px;margin-left:2px}

/* steps */
.steps{height:460px;padding:28px 160px 0}
.step-grid{display:grid;grid-template-columns:repeat(3,1fr);gap:20px 36px;margin-top:24px}
.step{position:relative}
.step .photo{height:132px;background:linear-gradient(135deg,#e5e1da,#b9b2a8)}
.step-no{position:absolute;top:10px;right:10px;width:34px;height:34px;border-radius:50%;background:var(--green);color:var(--white);font-size:17px;font-weight:700;display:flex;align-items:center;justify-content:center}
.step-label{font-size:13px;margin-top:6px}

/* voice */
.voice{height:540px;padding:20px 160px 0}
.voice-list{display:flex;gap:36px;margin-top:24px}
.voice-item{flex:1;text-align:center}
.voice-item .photo{height:230px;background:linear-gradient(135deg,#eceae6,#c7c2ba)}
.voice-quote{position:relative;margin:-40px 14px 0;background:var(--white);border:1px solid var(--line);padding:14px 16px 10px;text-align:left;font-size:17px;font-weight:700;line-height:1.5}
.voice-quote::before{content:"";position:absolute;left:12px;top:12px;bottom:12px;border-left:3px solid var(--orange)}
.voice-quote p{padding-left:10px}
.voice-name{display:block;text-align:right;font-size:13px;font-weight:500;margin-top:4px}
.btn-see{display:inline-block;margin-top:16px;border:1px solid var(--orange);color:var(--orange);font-size:11px;padding:3px 30px}

/* schedule */
.schedule-head{height:140px;padding-top:44px}
.schedule{position:relative;height:620px;background:linear-gradient(180deg,#6f5c4c 0%,#4b3d33 55%,#2f2722 100%);padding:40px 190px 0}
.schedule-list{position:relative;display:flex;flex-direction:column;gap:26px}
.event{height:112px;background:rgba(255,255,255,.94);display:flex;align-items:center;padding:0 30px}
.event-date{width:190px;display:flex;align-items:baseline;gap:8px;color:var(--sub)}
.event-date .year{font-size:15px}
.event-date .day{font-size:38px;font-weight:400;color:var(--ink)}
.event-date .wd{font-size:13px}
.event-name{flex:1;font-size:21px;font-weight:700;line-height:1.45;border-left:1px solid var(--line);padding-left:24px}
.event-note{width:230px;font-size:11px;color:var(--sub);line-height:1.7}
.event-new{position:absolute;left:-22px;top:-12px;width:44px;height:44px;background:var(--orange);color:var(--white);font-size:11px;font-weight:700;display:flex;align-items:center;justify-content:center;transform:rotate(-45deg)}

/* column */
.column{height:480px;padding-top:40px}
.column-list{display:flex;justify-content:center;gap:64px;margin-top:32px}
.column-item{width:180px;text-align:center;font-size:11px;color:var(--sub)}
.column-item .photo{width:160px;height:160px;border-radius:50%;margin:0 auto 12px;background:linear-gradient(135deg,#e9d8c6,#a98b70)}
.column-item .date{font-family:"Montserrat",sans-serif;color:var(--ink);margin-bottom:4px}

/* cta */
.cta{height:340px;background:var(--pale);display:flex;justify-content:center;gap:40px;padding-top:50px}
.cta-box{width:420px;height:240px;color:var(--white);text-align:center;padding-top:34px}
.cta-box.is-entry{background:var(--orange)}
.cta-box.is-doc{background:var(--green)}
.cta-label{font-size:17px;font-weight:500}
.cta-main{font-size:46px;font-weight:900;line-height:1.3;letter-spacing:.08em}
.cta-main span{font-weight:400;margin:0 12px}
.cta-btn{display:inline-block;margin-top:18px;background:var(--white);font-size:13px;font-weight:700;padding:6px 58px;border-radius:3px}
.is-entry .cta-btn{color:var(--orange)}
.is-doc .cta-btn{color:var(--green)}

/* footer */
.site-footer{height:360px;display:flex;padding:50px 70px 0;gap:50px;background:var(--footer)}
.footer-info{width:310px;font-size:11px;color:var(--sub);line-height:1.8}
.footer-info .brand{margin-bottom:18px}
.footer-nav{flex:1;display:grid;grid-template-columns:repeat(3,1fr);gap:0 30px;border-left:1px solid var(--line);padding-left:40px}
.footer-nav ul{list-style:none;font-size:12px;line-height:2.2}
.footer-nav li::before{content:"›";color:var(--orange);margin-right:6px}
.copyright{height:100px;background:var(--copy);color:var(--white);font-size:12px;display:flex;align-items:center;justify-content:center;letter-spacing:.1em}
</style>
</head>
<body>

<header class="site-header">
  <div class="brand">
    <span class="brand-mark"></span>
    <div class="brand-text"><small>経理・総務の未経験者専門の人材派遣</small><strong>そよかぜキャリア</strong></div>
  </div>
  <nav class="gnav">
    <span>そよかぜキャリアについて</span><span>スタッフ紹介</span><span>選ばれる理由</span><span>Q&amp;A</span><span>採用情報</span><span>会社概要</span>
  </nav>
</header>

<section class="hero">
  <div class="photo" role="img" aria-label="キーボードの上に座る会社員のミニチュア人形の写真" style="position:absolute;inset:0"></div>
  <h1 class="hero-copy">私達、未経験から<br>経理のプロになりました。</h1>
  <div class="hero-tabs">
    <div class="hero-tab is-seeker">経理未経験の方へ</div>
    <div class="hero-tab is-company">企業担当者様へ</div>
  </div>
</section>

<section class="intro">
  <div class="intro-body">
    <h2 class="intro-title">そよかぜキャリアは経理・総務に<br>特化した人材派遣会社です。</h2>
    <p class="intro-text">経理未経験の方でも安心して働けるよう、独自のカレッジで基礎から実務まで丁寧にお伝えします。代表自らが講師となり、一人ひとりのキャリアに寄り添いながら、就業後も継続してサポートいたします。東京23区を中心に、優良企業へのお仕事をご紹介しています。</p>
    <span class="btn-more">もっと詳しく</span>
  </div>
  <div class="photo" role="img" aria-label="オフィスで笑顔で話す女性社員たちの写真"></div>
</section>

<section class="strip">
  <div class="photo p1" role="img" aria-label="セミナー会場で講義を受ける受講生の写真"></div>
  <div class="photo p2" role="img" aria-label="ホワイトボードの前で説明する講師の写真"></div>
  <div class="photo p3" role="img" aria-label="セミナーで話す女性スタッフの写真"></div>
</section>

<section class="reasons">
  <h2 class="sec-title">そよかぜキャリアが選ばれる理由</h2>
  <span class="sec-sub en">REASONS</span>
  <div class="reason-list">
    <div class="reason"><span class="reason-label">未経験者の<br>就業率</span><span class="reason-num en">98<span>%</span></span></div>
    <div class="reason"><span class="reason-label">未経験者の<br>紹介実績企業</span><span class="reason-num en">25<span>社</span></span></div>
    <div class="reason"><span class="reason-label">ママの社員<br>登録者数</span><span class="reason-num en">8<span>名</span></span></div>
    <div class="reason"><span class="reason-label">紹介予定<br>派遣成約率</span><span class="reason-num en">55<span>%</span></span></div>
  </div>
</section>

<section class="steps">
  <h2 class="sec-title">就職までのステップ</h2>
  <span class="sec-sub en">STEP TO EMPLOYMENT</span>
  <div class="step-grid">
    <div class="step"><div class="photo" role="img" aria-label="書類に記入する手元の写真"></div><span class="step-no en">1</span><p class="step-label">登録する</p></div>
    <div class="step"><div class="photo" role="img" aria-label="セミナーを受講する人々の写真"></div><span class="step-no en">2</span><p class="step-label">セミナー（そよかぜカレッジ）受講</p></div>
    <div class="step"><div class="photo" role="img" aria-label="面談で仕事を紹介するスタッフの写真"></div><span class="step-no en">3</span><p class="step-label">仕事紹介</p></div>
    <div class="step"><div class="photo" role="img" aria-label="握手を交わすビジネスパーソンの写真"></div><span class="step-no en">4</span><p class="step-label">雇用契約</p></div>
    <div class="step"><div class="photo" role="img" aria-label="パソコンで仕事をする手元の写真"></div><span class="step-no en">5</span><p class="step-label">就業スタート</p></div>
    <div class="step"><div class="photo" role="img" aria-label="笑顔で相談に応じるスタッフの写真"></div><span class="step-no en">6</span><p class="step-label">アフターフォロー</p></div>
  </div>
</section>

<section class="voice">
  <h2 class="sec-title">カレッジ卒業生の声</h2>
  <span class="sec-sub en">VOICE</span>
  <div class="voice-list">
    <div class="voice-item">
      <div class="photo" role="img" aria-label="卒業生のポートレート写真"></div>
      <div class="voice-quote"><p>セミナーの参加がキャリアアップにつながりました。</p><span class="voice-name">A子さん</span></div>
      <span class="btn-see en">SEE MORE</span>
    </div>
    <div class="voice-item">
      <div class="photo" role="img" aria-label="卒業生のポートレート写真"></div>
      <div class="voice-quote"><p>セミナーの参加がキャリアアップにつながりました。</p><span class="voice-name">Bさん</span></div>
      <span class="btn-see en">SEE MORE</span>
    </div>
    <div class="voice-item">
      <div class="photo" role="img" aria-label="卒業生のポートレート写真"></div>
      <div class="voice-quote"><p>セミナーの参加がキャリアアップにつながりました。</p><span class="voice-name">Cさん</span></div>
      <span class="btn-see en">SEE MORE</span>
    </div>
  </div>
</section>

<div class="schedule-head">
  <h2 class="sec-title">そよかぜカレッジ日程</h2>
  <span class="sec-sub en">SCHEDULE</span>
</div>
<section class="schedule" role="img" aria-label="温かい照明のオフィス受付の写真を背景にした開催日程">
  <div class="schedule-list">
    <div class="event" style="position:relative">
      <span class="event-new en">NEW</span>
      <div class="event-date en"><span class="year">2019</span><span class="day">4/25</span><span class="wd">sat</span></div>
      <p class="event-name">経理・総務セミナー</p>
      <p class="event-note">初心者向けの基礎講座です。<br>仕訳の考え方から学べます。<br>会場：本社セミナールーム</p>
    </div>
    <div class="event">
      <div class="event-date en"><span class="year">2019</span><span class="day">5/11</span><span class="wd">sat</span></div>
      <p class="event-name">「経理のレベルアップ」<br>セミナー</p>
      <p class="event-note">月次決算の流れを解説します。<br>実務に役立つ内容です。<br>会場：本社セミナールーム</p>
    </div>
    <div class="event">
      <div class="event-date en"><span class="year">2019</span><span class="day">5/25</span><span class="wd">sat</span></div>
      <p class="event-name">「小さな会社の総務の<br>実務」徹底解説セミナー</p>
      <p class="event-note">総務の仕事を幅広く学べます。<br>書類作成の演習つきです。<br>会場：本社セミナールーム</p>
    </div>
    <div class="event">
      <div class="event-date en"><span class="year">2019</span><span class="day">6/2</span><span class="wd">sat</span></div>
      <p class="event-name">経理・総務セミナー</p>
      <p class="event-note">初心者向けの基礎講座です。<br>仕訳の考え方から学べます。<br>会場：本社セミナールーム</p>
    </div>
  </div>
</section>

<section class="column">
  <h2 class="sec-title">そよかぜコラム</h2>
  <span class="sec-sub en">COLUMN</span>
  <div class="column-list">
    <div class="column-item"><div class="photo" role="img" aria-label="オフィスの受付の写真"></div><p class="date">2019.10/31</p><p>経理の基本を<br>やさしく解説します</p></div>
    <div class="column-item"><div class="photo" role="img" aria-label="面談するスタッフの写真"></div><p class="date">2019.10/31</p><p>未経験からの<br>転職成功のコツ</p></div>
    <div class="column-item"><div class="photo" role="img" aria-label="セミナーで話す講師の写真"></div><p class="date">2019.10/31</p><p>カレッジ講義の<br>様子をお届けします</p></div>
    <div class="column-item"><div class="photo" role="img" aria-label="書道作品の飾られた室内の写真"></div><p class="date">2019.10/31</p><p>代表からの<br>メッセージ</p></div>
  </div>
</section>

<section class="cta">
  <div class="cta-box is-entry">
    <p class="cta-label">そよかぜカレッジ</p>
    <p class="cta-main"><span>[</span>エントリー<span>]</span></p>
    <span class="cta-btn">入力フォームへ</span>
  </div>
  <div class="cta-box is-doc">
    <p class="cta-label">そよかぜカレッジ</p>
    <p class="cta-main" style="font-size:40px"><span>[</span>資料ダウンロード<span>]</span></p>
    <span class="cta-btn">入力フォームへ</span>
  </div>
</section>

<footer class="site-footer">
  <div class="footer-info">
    <div class="brand">
      <span class="brand-mark"></span>
      <div class="brand-text"><small>経理・総務の未経験者専門の人材派遣</small><strong>そよかぜキャリア</strong></div>
    </div>
    <p>〒100-0000<br>東京都千代田区みどり町1-2-3 そよかぜビル5F<br>TEL 03-0000-1234</p>
  </div>
  <nav class="footer-nav">
    <ul><li>そよかぜキャリアについて</li><li>スタッフ紹介</li><li>選ばれる理由</li><li>就職までのステップ</li><li>卒業生の声</li></ul>
    <ul><li>未経験者の方へ</li><li>そよかぜカレッジ日程</li><li>そよかぜコラム</li><li>よくあるご質問</li><li>採用情報</li></ul>
    <ul><li>企業担当者様へ</li><li>会社概要</li><li>個人情報保護方針</li><li>お問い合わせ</li></ul>
  </nav>
</footer>
<div class="copyright en">COPYRIGHT © SOYOKAZE CAREER ALL RIGHTS RESERVED.</div>

</body>
</html>
```